" Somos uma escola de Yoga e oferecemos aulas, Cursos de Formaçao para Professores de Yoga, workshops e retiros de meditaçao pelo Brasil e em países como Costa Rica, Panamá, Bali e Tailandia. Trabalhamos com o metodo Yin e Yang.. onde yin é a energia da meditaçao, contemplaçao e observaçao e yang do movimento, rítmo, força e atividade. "

```html
<!DOCTYPE html>
<html lang="pt-BR">
<head>
<meta charset="utf-8">
<title>Assinatura de e-mail — Casa Aurora</title>
<link href="https://fonts.googleapis.com/css2?family=Roboto:wght@400;700&display=swap" rel="stylesheet">
<style>
  :root {
    --page: #ecebe7;
    --green: #79b33f;
    --green-dark: #5e9a2c;
    --green-light: #9ccc5c;
    --white: #ffffff;
    --ink: #3a3a3a;
  }
  * { margin: 0; padding: 0; box-sizing: border-box; }
  html, body {
    width: 1200px; height: 1200px; overflow: hidden;
    background: var(--page);
    font-family: "Roboto", Arial, sans-serif;
  }
  .signature {
    position: absolute; left: 115px; top: 485px;
    width: 970px; height: 226px;
    background: var(--white);
    box-shadow: 0 6px 18px rgba(0,0,0,.18);
    overflow: hidden;
  }
  .signature__band { position: absolute; inset: 0; width: 100%; height: 100%; }
  .contact {
    position: absolute; left: 0; top: 0; width: 520px; height: 100%;
    color: var(--white);
  }
  .contact__name {
    position: absolute; left: 150px; top: 38px;
    font-weight: 700; font-size: 24px; letter-spacing: .2px;
  }
  .contact__role {
    position: absolute; left: 232px; top: 70px;
    font-size: 12px;
  }
  .contact__grid {
    position: absolute; left: 98px; top: 124px;
    list-style: none;
    display: grid; grid-template-columns: 158px 170px;
    row-gap: 11px; column-gap: 4px;
    font-size: 12.5px;
  }
  .contact__item { display: flex; align-items: center; gap: 7px; white-space: nowrap; }
  .contact__icon {
    width: 17px; height: 17px; border-radius: 50%;
    background: var(--white); flex: none;
    display: flex; align-items: center; justify-content: center;
  }
  .contact__icon svg { width: 11px; height: 11px; }
  .brand {
    position: absolute; left: 640px; top: 38px; width: 280px;
    display: flex; flex-direction: column; align-items: center;
  }
  .brand__mark {
    width: 100px; height: 100px; border-radius: 50%;
    background: var(--green);
  }
  .brand__name {
    margin-top: 14px; font-size: 30px; font-weight: 400;
    color: var(--ink); letter-spacing: .3px;
  }
</style>
</head>
<body>
  <section class="signature" aria-label="Assinatura de e-mail">
    <svg class="signature__band" viewBox="0 0 970 226" preserveAspectRatio="none" aria-hidden="true">
      <defs>
        <linearGradient id="band-green" x1="0" y1="0" x2="1" y2="0">
          <stop offset="0" stop-color="#84bb48"/>
          <stop offset="1" stop-color="#6ea837"/>
        </linearGradient>
      </defs>
      <polygon points="0,0 465,0 580,226 0,226" fill="url(#band-green)"/>
      <polygon points="465,0 490,0 605,226 580,226" fill="var(--green-light)"/>
      <polygon points="490,0 505,0 620,226 605,226" fill="var(--green-dark)"/>
    </svg>

    <div class="contact">
      <h1 class="contact__name">Tiago M. Ribeiro</h1>
      <p class="contact__role">Gerente</p>
      <ul class="contact__grid">
        <li class="contact__item"><span class="contact__icon"></span>+55 11 9000-2211</li>
        <li class="contact__item"><span class="contact__icon">
          <svg viewBox="0 0 24 24"><path fill="#6ea837" d="M6.6 10.8a15.1 15.1 0 0 0 6.6 6.6l2.2-2.2a1 1 0 0 1 1-.25 11.4 11.4 0 0 0 3.6.57 1 1 0 0 1 1 1V20a1 1 0 0 1-1 1A17 17 0 0 1 3 4a1 1 0 0 1 1-1h3.5a1 1 0 0 1 1 1c0 1.25.2 2.45.57 3.57a1 1 0 0 1-.25 1z"/></svg>
        </span>+55 11 3000-4422</li>
        <li class="contact__item"><span class="contact__icon"></span>@casaaurora</li>
        <li class="contact__item"><span class="contact__icon"></span>/casaaurora</li>
        <li class="contact__item"><span class="contact__icon"></span>casaaurora.com.br</li>
        <li class="contact__item"><span class="contact__icon">
          <svg viewBox="0 0 24 24"><path fill="#6ea837" d="M12 2a7 7 0 0 0-7 7c0 5.2 7 13 7 13s7-7.8 7-13a7 7 0 0 0-7-7zm0 9.5A2.5 2.5 0 1 1 12 6.5a2.5 2.5 0 0 1 0 5z"/></svg>
        </span>R. das Flores, 120, SP</li>
      </ul>
    </div>

    <div class="brand">
      <div class="brand__mark" aria-hidden="true"></div>
      <p class="brand__name">Casa Aurora</p>
    </div>
  </section>
</body>
</html>
```